We need a logo for our business which is a dental clinic (i.e. dentistry).
We would lilke designs using the colour blue, green and black incorporating the words Corvasta Dental, possibly a smile or a tooth image can be considered for incorporation in the logo.

Industry/Entity Type

Dental

```html
<!DOCTYPE html>
<html lang="en">
<head>
<meta charset="utf-8">
<title>Corvasta Dental – Business Card</title>
<link rel="stylesheet" href="https://fonts.googleapis.com/css2?family=Exo+2:wght@400;500;600&display=swap">
<style>
  :root {
    --page-bg: #e9ecef;
    --card-white: #ffffff;
    --card-shade: #f1f3f4;
    --blue-light: #8adaf3;
    --blue-deep: #2fb0d6;
    --accent-green: #a9d33a;
    --brand-blue: #2aa3cc;
    --ink: #17262e;
  }
  * { margin: 0; padding: 0; box-sizing: border-box; }
  html, body {
    width: 1200px; height: 900px; overflow: hidden;
    background: var(--page-bg);
    font-family: "Exo 2", sans-serif;
  }
  .business-card {
    position: absolute; left: 110px; top: 170px;
    width: 980px; height: 560px;
    border-radius: 40px; overflow: hidden;
    background: linear-gradient(135deg, var(--card-white) 0%, var(--card-shade) 100%);
    box-shadow: 0 18px 40px rgba(0,0,0,0.18);
  }
  .card-shapes { position: absolute; inset: 0; }
  .brand-lockup {
    position: absolute; left: 70px; top: 250px;
    display: flex; align-items: center; gap: 16px;
  }
  .brand-dot {
    width: 30px; height: 30px; border-radius: 50%;
    background: var(--brand-blue);
  }
  .brand-name {
    font-weight: 600; font-size: 38px; color: var(--brand-blue);
    letter-spacing: 0.5px;
  }
  .contact-block {
    position: absolute; right: 62px; top: 56px;
    text-align: right; color: var(--ink);
  }
  .person-name { font-size: 28px; font-weight: 500; letter-spacing: 1.5px; text-transform: uppercase; }
  .person-role { font-size: 18px; letter-spacing: 1.5px; margin-top: 4px; text-transform: uppercase; }
  .address { font-size: 22px; line-height: 1.3; margin-top: 62px; }
  .contact-list { list-style: none; margin-top: 44px; }
  .contact-list li {
    display: flex; justify-content: flex-end; align-items: center; gap: 10px;
    font-size: 21px; letter-spacing: 1px; height: 42px;
  }
  .contact-list li.small { font-size: 19px; letter-spacing: 0.5px; height: 38px; }
  .contact-list svg { width: 20px; height: 20px; fill: var(--ink); }
  .contact-list .no-icon { width: 20px; }
</style>
</head>
<body>
  <div class="business-card">
    <svg class="card-shapes" viewBox="0 0 980 560" aria-hidden="true">
      <defs>
        <radialGradient id="blueGlow" cx="0.62" cy="0.55" r="0.6">
          <stop offset="0" stop-color="var(--blue-light)"/>
          <stop offset="1" stop-color="var(--blue-deep)"/>
        </radialGradient>
      </defs>
      <path d="M300 0 C 500 110, 560 380, 420 560 L 980 560 L 980 0 Z" fill="var(--accent-green)"/>
      <path d="M340 0 C 540 110, 590 380, 452 560 L 980 560 L 980 0 Z" fill="url(#blueGlow)"/>
    </svg>

    <div class="brand-lockup">
      <span class="brand-dot"></span>
      <span class="brand-name">Corvasta Dental</span>
    </div>

    <div class="contact-block">
      <p class="person-name">Dana Whitfield</p>
      <p class="person-role">President</p>
      <p class="address">214, 9th floor, Harbor<br>Lane Road NTX</p>
      <ul class="contact-list">
        <li>020 555 0147
          <svg viewBox="0 0 24 24"><path d="M6.6 10.8a15.1 15.1 0 0 0 6.6 6.6l2.2-2.2c.3-.3.7-.4 1-.2 1.1.4 2.3.6 3.6.6.6 0 1 .4 1 1V20c0 .6-.4 1-1 1A17 17 0 0 1 3 4c0-.6.4-1 1-1h3.5c.6 0 1 .4 1 1 0 1.3.2 2.5.6 3.6.1.3 0 .7-.2 1z"/></svg>
        </li>
        <li>020 555 0148
          <svg viewBox="0 0 24 24"><path d="M7 1h10a2 2 0 0 1 2 2v18a2 2 0 0 1-2 2H7a2 2 0 0 1-2-2V3a2 2 0 0 1 2-2zm0 3v14h10V4zm5 15.5a1 1 0 1 0 0 2 1 1 0 0 0 0-2z"/></svg>
        </li>
        <li>020 555 0149
          <svg viewBox="0 0 24 24"><path d="M6 2h9l3 3v4h1a3 3 0 0 1 3 3v7h-4v3H6v-3H2v-7a3 3 0 0 1 3-3h1zm2 2v5h8V6h-2V4zm0 12v4h8v-4z"/></svg>
        </li>
        <li class="small">hello@corvasta.com
          <svg viewBox="0 0 24 24"><path d="M2 5h20v14H2zm2 2v.5l8 5 8-5V7zm0 2.8V17h16V9.8l-8 5z"/></svg>
        </li>
        <li class="small">www.corvastadental.com
          <svg viewBox="0 0 24 24"><path d="M12 2a10 10 0 1 0 0 20 10 10 0 0 0 0-20zm6.9 6h-3a15 15 0 0 0-1.3-3.8A8 8 0 0 1 18.9 8zM12 4c.8 1.2 1.5 2.5 1.9 4h-3.8c.4-1.5 1.1-2.8 1.9-4zM4.3 14a8 8 0 0 1 0-4h3.4a16 16 0 0 0 0 4zm.8 2h3a15 15 0 0 0 1.3 3.8A8 8 0 0 1 5.1 16zm3-8h-3a8 8 0 0 1 4.3-3.8C8.8 5.4 8.4 6.7 8.1 8zM12 20c-.8-1.2-1.5-2.5-1.9-4h3.8c-.4 1.5-1.1 2.8-1.9 4zm2.3-6H9.7a14 14 0 0 1 0-4h4.6a14 14 0 0 1 0 4zm.3 5.8c.6-1.2 1-2.5 1.3-3.8h3a8 8 0 0 1-4.3 3.8zm1.7-5.8a16 16 0 0 0 0-4h3.4a8 8 0 0 1 0 4z"/></svg>
        </li>
      </ul>
    </div>
  </div>
</body>
</html>
```